Kelvo-Dex Flyer (Business Launch)

Using my existing log design for Kelvo-Dex Mobile Mechanics, I would like a flyer designed. This would be used for advertising, letterbox drops, handing to the public , door knocking ect.

I'm looking for clean cut simple though with the wow factor, I was thinking of even having the flyer in the shape of a van to promote that I'm a mobile business (I come to you ect)

I've attached copies of my logo and business cards.

I would like the following list of services we provide listed on the flyer (see back of business card).
7 day service (we come to you)
10% discount for online/email booking-enquiry

I think this should be enough for now.

I'm launching this business to aiming to hit the ground running,

Target Market(s)

All motor vehicle owners, house holds, businesses

Industry/Entity Type

Automotive

Font styles to use
Sans Serif
Other font styles liked:
• refer images

Colors
0355a3

Requirements
Must have
• services offered, logo, 7 days, we come to or or catchy phrase to let people know this.
• 10% discount for online/email booking enquiries
• Maintenance Package Servicing from $149 conditions apply
• my preference is for blue, grey and while colour scheme, though also happy to accept artistic design ideas to these.
Nice to have
• Wow factor, brochure that stand out from the rest
• Different share brochure in shape of work van (refer varsona kribo van)
Should not have
• Not looking for a cheap quick fix, I'm wanting to create a brand .

```html
<!DOCTYPE html>
<html lang="en">
<head>
<meta charset="utf-8">
<title>Kelvo-Dex Mobile Mechanics Flyer</title>
<link rel="stylesheet" href="https://fonts.googleapis.com/css2?family=Aldrich&family=Montserrat:wght@700&family=Oswald:wght@300;500&family=Questrial&family=Source+Sans+3:wght@700&display=swap">
<style>
  :root {
    --brand-blue: #0355a3;
    --blue-light: #4f8ad0;
    --blue-mid: #2a64b8;
    --offer-blue: #7fb0ea;
    --ink: #1c1c1c;
    --logo-ink: #2b2b2b;
    --logo-grey: #8a8a8a;
    --mark-blue: #4a7fc4;
    --paper: #ffffff;
    --footer: #1b1b1b;
    --footer-grey: #8c8c8c;
    --stage: #e8e8e8;
  }
  * { margin: 0; padding: 0; box-sizing: border-box; }
  html, body {
    width: 1200px; height: 1200px; overflow: hidden;
    background: var(--stage);
  }
  .flyer {
    position: absolute; left: 205px; top: 40px;
    width: 790px; height: 1120px;
    background: var(--paper);
    overflow: hidden;
  }
  .flyer-bands { position: absolute; inset: 0; }
  .brand {
    position: absolute; left: 178px; top: 36px;
    display: flex; align-items: center; gap: 22px;
  }
  .brand-dot {
    width: 84px; height: 84px; border-radius: 50%;
    background: var(--mark-blue);
  }
  .brand-name {
    font-family: "Montserrat", sans-serif; font-weight: 700;
    font-size: 64px; line-height: 1; color: var(--logo-ink);
    letter-spacing: -1px;
  }
  .brand-tagline {
    font-family: "Montserrat", sans-serif; font-weight: 700;
    font-size: 26px; line-height: 1; color: var(--logo-grey);
    margin-top: 8px; letter-spacing: 0.5px;
  }
  .headline {
    position: absolute; left: 0; right: 0; top: 222px;
    text-align: center;
    font-family: "Source Sans 3", sans-serif; font-weight: 700;
    font-size: 84px; line-height: 1; color: var(--paper);
    letter-spacing: -0.5px;
  }
  .days {
    position: absolute; left: 0; right: 0; top: 316px;
    display: flex; align-items: center; justify-content: center; gap: 8px;
    font-family: "Oswald", sans-serif; font-weight: 300;
    font-size: 56px; line-height: 1; color: var(--paper);
    text-transform: uppercase;
  }
  .days-rule { width: 90px; height: 3px; background: var(--paper); }
  .phone-photo {
    position: absolute; left: 0; top: 384px;
    width: 285px; height: 356px;
    background: radial-gradient(ellipse at 55% 45%, #5a5a70 0%, #2c2c36 55%, rgba(210,170,140,0.9) 100%);
    border-radius: 0 40px 40px 0;
  }
  .services {
    position: absolute; left: 307px; top: 400px;
    list-style: none;
    font-family: "Aldrich", sans-serif;
    font-size: 32px; line-height: 44px; color: var(--ink);
    letter-spacing: 1.5px;
  }
  .services li { margin-bottom: 14px; }
  .service-note {
    display: block;
    font-size: 20px; line-height: 26px; color: var(--paper);
    letter-spacing: 1px;
  }
  .principal {
    position: absolute; left: 250px; width: 440px; top: 762px;
    text-align: center;
  }
  .principal-name {
    font-family: "Oswald", sans-serif; font-weight: 500;
    font-size: 52px; line-height: 1; color: var(--ink);
  }
  .principal-role {
    font-family: "Oswald", sans-serif; font-weight: 300;
    font-size: 30px; line-height: 1; color: var(--paper);
    letter-spacing: 3px; margin-top: 8px;
  }
  .contact {
    position: absolute; left: 0; right: 0; top: 918px;
    text-align: center; color: var(--paper);
    font-family: "Questrial", sans-serif;
  }
  .contact-offer {
    font-size: 21px; line-height: 30px; color: var(--offer-blue);
    letter-spacing: 0.5px; margin-bottom: 4px;
  }
  .contact-phone { font-size: 28px; line-height: 38px; }
  .contact-web { font-size: 19px; line-height: 25px; }
  .contact-web.first { margin-top: 6px; }
  .abn {
    position: absolute; left: 0; right: 0; top: 1090px;
    text-align: center; color: var(--footer-grey);
    font-family: "Questrial", sans-serif;
    font-size: 17px; letter-spacing: 2px;
  }
</style>
</head>
<body>
  <main class="flyer">
    <svg class="flyer-bands" width="790" height="1120" viewBox="0 0 790 1120" aria-hidden="true">
      <defs>
        <radialGradient id="blueGlow" cx="0.6" cy="0.5" r="0.75">
          <stop offset="0" stop-color="var(--blue-light)"/>
          <stop offset="0.55" stop-color="var(--blue-mid)"/>
          <stop offset="1" stop-color="var(--brand-blue)"/>
        </radialGradient>
      </defs>
      <path fill="url(#blueGlow)" d="M0,205 L22,190 48,201 70,186 96,198 122,184 150,200 178,189 205,203 232,186 262,199 290,185 320,201 350,188 380,204 410,190 440,199 470,185 500,202 530,189 560,203 590,187 620,200 650,186 680,203 710,190 740,201 765,188 790,196 L790,1000 L0,1000 Z"/>
      <path fill="var(--footer)" d="M0,900 L25,887 52,895 80,879 110,891 140,877 170,893 200,882 232,894 262,878 295,890 325,876 355,892 388,880 420,893 452,877 485,889 515,875 548,888 580,874 612,887 645,873 678,885 710,872 745,883 770,871 790,879 L790,1120 L0,1120 Z"/>
    </svg>

    <header class="brand">
      <div class="brand-dot"></div>
      <div>
        <div class="brand-name">Kelvo-Dex</div>
        <div class="brand-tagline">MOBILE MECHANICS</div>
      </div>
    </header>

    <h1 class="headline">MOBILE SERVICE</h1>
    <p class="days"><span class="days-rule"></span>7 Days a Week<span class="days-rule"></span></p>

    <div class="phone-photo" role="img" aria-label="Photo of a hand holding a smartphone showing its home screen"></div>

    <ul class="services">
      <li>Servicing and Repairs</li>
      <li>Manufacturers<br>Log Book Service</li>
      <li>Maintenance<br>Package Service<span class="service-note">From $149 – conditions apply</span></li>
      <li>Pre-Purchase Inspections</li>
    </ul>

    <div class="principal">
      <p class="principal-name">Darren Holloway</p>
      <p class="principal-role">PRINCIPAL</p>
    </div>

    <footer class="contact">
      <p class="contact-offer">10% off all online / email booking enquiries</p>
      <p class="contact-phone">Tel : 1300 482 706</p>
      <p class="contact-phone">Mob : 0412 367 590</p>
      <p class="contact-web first">E-mail : admin@kelvo-dex.com.au</p>
      <p class="contact-web">Website : www.kelvo-dex.com.au</p>
    </footer>
    <p class="abn">ABN 48615 092 337</p>
  </main>
</body>
</html>
```